Business Card for a Life Coaching Company

BRAVOPEAK is a Life Coaching company that was initiated to support people who want to transform thier life or ana aspect of it.
our slogan is : "Dream. Believe. Succeed"
our logo is uploaded.
The name of the company implies that leadership, strength and wisdom required to change your life.
We want an attractive business card that would give an impression of reliability, support and change. so we really want it unique. Here are some examples of unique cards:

http://www.cardcraftvault.example/2009/05/100-really-creative-business-cards/

BravoPeak is a life coaching organization focusing on individual transformation through the application of relevant and timeless principles of success.  BravoPeak believes that real, sustainable life transformations are brought about by tuning into the timeless wisdom we each carry in our hearts while boldy acting in the direction of our dreams.

Contacts on the card:
Address: 7 Tarek Nour El Dine Heliopolis Cairo Egypt
Tel: +202 24 71 38 52
Fax: +202 24 71 38 17
Mobile: +2 012 684 2097 (Dalia Soliman)
+2 0199915815 (Tariq Bhatti)

By the way, our temporary website is http://www.bravopeak.example

We have attached an .eps file with various configurations of our logo.

```html
<!DOCTYPE html>
<html lang="en">
<head>
<meta charset="utf-8">
<title>BravoPeak Business Cards</title>
<link rel="stylesheet" href="https://fonts.googleapis.com/css2?family=EB+Garamond:wght@400&display=swap">
<style>
  :root {
    --page: #ffffff;
    --stage: #000000;
    --card-light: #ffffff;
    --brand-orange: #f47f20;
    --stripe-orange: #f7941d;
    --band-light: #f8a35c;
    --band-dark: #e8621c;
    --fold: #fbb26e;
    --ink-light: #ffffff;
  }
  html, body {
    margin: 0;
    padding: 0;
    width: 1200px;
    height: 829px;
    overflow: hidden;
    background: var(--page);
  }
  .canvas {
    display: block;
    width: 1200px;
    height: 829px;
  }
  .stage { fill: var(--stage); }
  .card--front { fill: var(--card-light); }
  .card--back { fill: var(--brand-orange); }
  .stripe--orange { fill: var(--stripe-orange); }
  .stripe--white { fill: var(--ink-light); }
  .band--light { fill: var(--band-light); }
  .band--dark { fill: var(--band-dark); }
  .corner-fold { fill: var(--fold); }
  .brand-name,
  .tagline {
    font-family: "EB Garamond", Garamond, serif;
    font-weight: 400;
  }
  .brand-name { font-size: 38px; letter-spacing: 0.5px; }
  .tagline { font-size: 16.5px; }
  .ink--orange { fill: var(--stripe-orange); }
  .ink--white { fill: var(--ink-light); }
</style>
</head>
<body>
<svg class="canvas" viewBox="0 0 800 552.7" preserveAspectRatio="none" xmlns="http://www.w3.org/2000/svg" aria-label="BravoPeak business card, front and back">
  <defs>
    <clipPath id="back-card-shape">
      <path d="M268 319 H649 V480 Q649 496 622 503 Q596 511 556 511 H268 Z"/>
    </clipPath>
  </defs>

  <rect class="stage" x="155" y="44" width="645" height="508.7"/>

  <!-- Front card -->
  <g class="card-front">
    <path class="card--front" d="M248 67 H628 V228 Q628 244 600 251 Q566 260 505 260 H248 Z"/>
    <g class="stripes">
      <polygon class="stripe--orange" points="248,82 313,106 313,121 248,97"/>
      <polygon class="stripe--orange" points="248,118 313,142 313,157 248,133"/>
      <polygon class="stripe--orange" points="248,155 313,179 313,194 248,170"/>
      <polygon class="stripe--orange" points="248,192 313,216 313,231 248,207"/>
    </g>
    <rect class="ink--orange" x="356" y="122" width="50" height="50"/>
    <text class="brand-name ink--orange" x="415" y="138">BRAVO</text>
    <text class="brand-name ink--orange" x="415" y="180">PEAK</text>
    <text class="tagline ink--orange" x="361" y="210">Dream. Believe. Succeed</text>
  </g>

  <!-- Back card -->
  <g class="card-back">
    <path class="card--back" d="M268 319 H649 V480 Q649 496 622 503 Q596 511 556 511 H268 Z"/>
    <g clip-path="url(#back-card-shape)">
      <rect class="band--light" x="268" y="470" width="381" height="4"/>
      <rect class="band--dark" x="268" y="478" width="381" height="4"/>
      <rect class="band--dark" x="268" y="486" width="381" height="12"/>
      <polygon class="corner-fold" points="596,503 628,482 612,500"/>
    </g>
    <g class="stripes">
      <polygon class="stripe--white" points="268,334 333,358 333,373 268,349"/>
      <polygon class="stripe--white" points="268,371 333,395 333,410 268,386"/>
      <polygon class="stripe--white" points="268,408 333,432 333,447 268,423"/>
      <polygon class="stripe--white" points="268,445 333,469 333,478 268,460"/>
    </g>
    <rect class="ink--white" x="376" y="368" width="50" height="50"/>
    <text class="brand-name ink--white" x="436" y="384">BRAVO</text>
    <text class="brand-name ink--white" x="436" y="425">PEAK</text>
    <text class="tagline ink--white" x="383" y="458">Dream. Believe. Succeed</text>
  </g>
</svg>
</body>
</html>
```